Email mail merge - not a marketing email, this is an update email sent regularly to our members

HI I need a generic email designed to send out to our members, this is a tri-weekly (monday - updates - Wednesday - updates and Fridays - weekly round up.

we would like it to have within the mail body, 3 interactive, changeable boxes for example "quote of the week', 'top performer' and something else, It would be great if we can remove a box if and when we choose.
Our company is called Vr4lo Amusements or Vr4lo for short.
It needs to be in HTML to fit with our back office software.
We have all the logos for you already which I have included, I have also included our current email header.
our websites are...
vr4lam.cub - This is our members back end site.
vr4lam.com - This is our gaming site.
Please email me on derek@vr4lam.com if you have any queries

Target Market(s)

All of our members - We currently have over 400 but it is growing at an astronomical rate.

Industry/Entity Type

Marketing

Font styles to use
Serif
Decorative
Script

Requirements
Must have
• At least two interactive, changeable boxes/areas that I can put photo's or quotes in to. I would also like some guidelines as to how I change these myself.
• The colours should be inline with our vr4lam.club site.
Nice to have
• This is a positive email update so it needs to look clean and clear but vibrant, we are a unique company that is breaking records and is very successful.
• Our members have the ability and some already are earning vast sums of money.

```html
<!DOCTYPE html>
<html lang="en">
<head>
<meta charset="utf-8">
<title>Vr4lo Amusements – Member Update</title>
<link href="https://fonts.googleapis.com/css2?family=Lato:ital,wght@0,300;0,400;0,700;1,400&family=Patrick+Hand&display=swap" rel="stylesheet">
<style>
  :root {
    --page-bg: #f0eeef;
    --card-bg: #ffffff;
    --teal: #15b39b;
    --teal-dark: #0f9c86;
    --teal-pale: #e6f4f1;
    --ink: #333333;
    --ink-soft: #4a4a4a;
    --logo-grey: #9aa3a5;
    --white: #ffffff;
  }
  * { box-sizing: border-box; margin: 0; padding: 0; }
  html, body { width: 1200px; height: 2323px; overflow: hidden; }
  body { background: var(--page-bg); font-family: "Lato", sans-serif; color: var(--ink); position: relative; }
  .abs { position: absolute; }

  .preheader { top: 56px; left: 0; width: 1200px; text-align: center; font-size: 16px; color: var(--ink); }
  .preheader a { color: var(--teal-dark); font-style: italic; }

  .mail-card { left: 164px; top: 124px; width: 875px; height: 1984px; background: var(--card-bg);
    border-top: 5px solid var(--teal); border-bottom: 6px solid var(--teal); }

  .issue-date { top: 136px; right: 198px; font-size: 16px; font-weight: 700; color: var(--ink); }

  .brand-name { top: 160px; left: 203px; font-size: 46px; font-weight: 700; color: var(--logo-grey); letter-spacing: 1px; display: flex; align-items: center; gap: 12px; }
  .brand-name .mark { width: 14px; height: 14px; background: var(--teal); }

  .contact-chip { top: 167px; height: 42px; background: var(--teal-pale); border-left: 5px solid var(--teal);
    border-right: 1px solid #b9ddd5; border-top: 1px solid #b9ddd5; border-bottom: 1px solid #b9ddd5;
    display: flex; align-items: center; gap: 10px; padding-left: 16px; font-size: 16px; color: var(--ink); }
  .contact-chip.web { left: 584px; width: 233px; }
  .contact-chip.phone { left: 825px; width: 175px; }

  .hero { left: 203px; top: 249px; width: 799px; height: 345px;
    background: linear-gradient(180deg, #141c48 0%, #2a2f6a 45%, #3a2f5a 70%, #7a3a55 85%, #1e1f3a 100%); }
  .hero-tag { left: 203px; top: 365px; width: 238px; height: 169px; background: rgba(21,179,155,0.92); color: var(--white); }
  .hero-tag .place { position: absolute; left: 21px; top: 26px; font-size: 62px; font-weight: 300; line-height: 1; }
  .hero-tag .sub { position: absolute; left: 74px; top: 96px; font-size: 28px; font-weight: 400; }

  .tagline { top: 612px; left: 203px; width: 799px; text-align: center; font-size: 17px; font-weight: 700; color: var(--ink); }
  .tagline span { color: var(--teal); font-weight: 400; letter-spacing: 0.5px; }

  .intro { top: 654px; left: 203px; width: 799px; font-size: 15px; line-height: 25px; color: var(--ink-soft); }

  .btn { background: var(--teal); color: var(--white); font-size: 14px; font-weight: 700; text-align: center;
    display: flex; align-items: center; justify-content: center; gap: 10px; text-transform: uppercase; }
  .btn-read { left: 526px; top: 740px; width: 149px; height: 46px; }

  .offer-box { left: 203px; top: 824px; width: 799px; height: 275px;
    background: radial-gradient(circle at 88% 55%, #7a1f2a 0%, #2b5a3e 22%, transparent 40%),
      linear-gradient(160deg, #16303a 0%, #14523c 50%, #0f4a34 100%); }
  .offer-title { left: 238px; top: 852px; font-size: 30px; color: var(--white); font-weight: 400; }
  .offer-text { left: 238px; top: 898px; width: 600px; font-size: 15px; line-height: 24px; color: var(--white); }
  .offer-more { left: 238px; top: 978px; font-size: 15px; color: var(--white); }
  .btn-performer { left: 237px; top: 1016px; width: 354px; height: 38px; font-size: 14px; }

  .invite { left: 203px; top: 1138px; width: 308px; font-size: 15px; line-height: 23px; color: var(--ink); }
  .invite p + p { margin-top: 8px; }
  .devices { left: 203px; top: 1323px; width: 254px; height: 109px;
    background: linear-gradient(180deg, #3a3a3a 0%, #1c1c1c 60%, #9a9a9a 100%); border-radius: 4px; }

  .club-panel { left: 536px; top: 1125px; width: 466px; height: 304px; background: var(--teal); color: var(--white); overflow: hidden; }
  .club-title { position: absolute; left: 26px; top: 18px; font-size: 35px; font-weight: 400; }
  .club-sub { position: absolute; left: 26px; top: 66px; font-size: 15px; line-height: 22px; color: #12362f; text-transform: uppercase; }
  .club-note { position: absolute; left: 280px; top: 33px; width: 180px; font-size: 13.5px; line-height: 20px; font-style: italic; }
  .club-list { position: absolute; left: 26px; top: 122px; list-style: none; display: grid;
    grid-template-columns: 128px 140px; row-gap: 11px; }
  .club-list li { display: flex; align-items: center; gap: 8px; font-size: 14.5px; height: 22px; }
  .agent { position: absolute; left: 292px; top: 86px; width: 174px; height: 218px;
    background: linear-gradient(180deg, #e8d0b8 0%, #f4efe9 45%, #ffffff 100%); border-radius: 80px 80px 0 0; }

  .join-badge { left: 203px; top: 1467px; width: 134px; height: 96px; background: var(--teal); overflow: hidden; }
  .join-badge span { position: absolute; left: 18px; top: 40px; transform: rotate(-40deg); color: var(--white);
    font-weight: 700; font-size: 17px; letter-spacing: 0.5px; }
  .join-text { left: 353px; top: 1460px; width: 640px; font-size: 17px; line-height: 22px; color: var(--ink); }
  .packages-lead { left: 351px; top: 1538px; font-family: "Patrick Hand", cursive; font-size: 19px; color: var(--ink); }
  .packages { left: 311px; top: 1578px; display: flex; gap: 20px; list-style: none; font-size: 17px; color: var(--ink); }
  .packages li { display: flex; align-items: center; gap: 5px; }
  .packages li::before { content: ""; width: 10px; height: 10px; background: var(--teal); }

  .stat-band { left: 241px; top: 1624px; width: 723px; height: 94px; background: var(--teal); color: var(--white); text-align: center; }
  .stat-band .lead { margin-top: 18px; font-size: 20px; }
  .stat-band .figure { font-size: 34px; line-height: 40px; }

  .closing { left: 241px; top: 1758px; width: 722px; font-size: 17px; line-height: 25px; color: var(--ink-soft); }
  .btn-join { left: 424px; top: 1865px; width: 353px; height: 39px; font-size: 14.5px; }

  .divider { left: 203px; top: 1943px; width: 799px; border-top: 2px dotted #b8b8b8; }

  .social-lead { left: 470px; top: 1968px; width: 260px; text-align: center; font-family: "Patrick Hand", cursive; font-size: 20px; color: var(--teal); letter-spacing: 0.5px; }
  .social-row { left: 522px; top: 2005px; display: flex; gap: 10px; list-style: none; }
  .social-row li { width: 33px; height: 33px; border-radius: 50%; background: var(--teal-dark); }
  .footer-brand { left: 774px; top: 2000px; font-size: 34px; font-weight: 700; color: var(--logo-grey); display: flex; align-items: center; gap: 9px; }
  .footer-brand .mark { width: 11px; height: 11px; background: var(--teal); }
  .copyright { left: 164px; top: 2056px; width: 875px; text-align: center; font-size: 16px; color: var(--ink); }
</style>
</head>
<body>
  <p class="abs preheader">For anything about this mail you can contract us by <a href="#">click this link.</a></p>

  <div class="abs mail-card"></div>

  <p class="abs issue-date">July 8, 2016</p>
  <div class="abs brand-name"><span>VR4LO ENT</span><span class="mark"></span></div>

  <div class="abs contact-chip web">
    <svg width="20" height="16" viewBox="0 0 20 16"><rect x="1" y="2" width="18" height="13" fill="none" stroke="#333" stroke-width="2"/><path d="M1 2 L10 9 L19 2" fill="none" stroke="#333" stroke-width="2"/></svg>
    <span>Contact vr4lam.com</span>
  </div>
  <div class="abs contact-chip phone">
    <svg width="20" height="20" viewBox="0 0 20 20"><path d="M4 2 L8 2 L9 6 L7 8 Q9 12 12 13 L14 11 L18 12 L18 16 Q17 18 14 18 Q4 15 2 5 Q2 2 4 2 Z" fill="none" stroke="#333" stroke-width="1.6"/></svg>
    <span>1300 555 018</span>
  </div>

  <div class="abs hero" role="img" aria-label="Night photograph of a harbour city skyline with a lit bridge and towers"></div>
  <div class="abs hero-tag"><span class="place">Marau</span><span class="sub">promotion</span></div>

  <p class="abs tagline">we are <span>BRINGING GAMING &amp; NETWORKING TOGETHER</span></p>
  <p class="abs intro">VR4LO CLUB is a package experience that encases decades of proven and time-tested service in two interlinked but rarely combined industries: networking and gaming. The company is driven by a team that's been experiencing and following the networking industry since the 1990s and the gaming industry since the 1980s... ....</p>
  <a class="abs btn btn-read">Read more&gt;</a>

  <div class="abs offer-box" role="img" aria-label="Photograph of casino chips on a green gaming table"></div>
  <h2 class="abs offer-title">Enjoy A priceless offer Miss it at your own peril! :</h2>
  <p class="abs offer-text">VR4LO ENT assures all your referred participants a safe gaming experience without compromising on the associated spills and thrills. They gain from our rewards programs just as you do, which results in a win-win situation ....</p>
  <p class="abs offer-more">READ MORE&gt;</p>
  <a class="abs btn btn-performer">Find out top performer of the weeks</a>

  <div class="abs invite">
    <p>We invite you to be a part of this epicenter of licensed betting and gaming, and pocket part of this monetary spoil! Once you join, you'll know what you've missed all along!</p>
    <p>Here are some unique advantages of becoming part of the growing VR4LO CLUB community accessible on all devices</p>
  </div>
  <div class="abs devices" role="img" aria-label="Laptop, tablet and phone showing the gaming site"></div>

  <section class="abs club-panel">
    <h2 class="club-title">VR4LO CLUB</h2>
    <p class="club-sub">The single-stop betting<br>and gaming platform</p>
    <p class="club-note">We are always on the button, answering all your queries</p>
    <ul class="club-list">
      <li><svg width="14" height="12" viewBox="0 0 14 12"><path d="M1 6 L5 10 L13 1" fill="none" stroke="#fff" stroke-width="2"/></svg>Professional</li>
      <li><svg width="14" height="12" viewBox="0 0 14 12"><path d="M1 6 L5 10 L13 1" fill="none" stroke="#fff" stroke-width="2"/></svg>Referral Rewards</li>
      <li><svg width="14" height="12" viewBox="0 0 14 12"><path d="M1 6 L5 10 L13 1" fill="none" stroke="#fff" stroke-width="2"/></svg>Protected</li>
      <li><svg width="14" height="12" viewBox="0 0 14 12"><path d="M1 6 L5 10 L13 1" fill="none" stroke="#fff" stroke-width="2"/></svg>Paid to Play</li>
      <li><svg width="14" height="12" viewBox="0 0 14 12"><path d="M1 6 L5 10 L13 1" fill="none" stroke="#fff" stroke-width="2"/></svg>The Gaming</li>
      <li><svg width="14" height="12" viewBox="0 0 14 12"><path d="M1 6 L5 10 L13 1" fill="none" stroke="#fff" stroke-width="2"/></svg>Low Risk</li>
      <li><svg width="14" height="12" viewBox="0 0 14 12"><path d="M1 6 L5 10 L13 1" fill="none" stroke="#fff" stroke-width="2"/></svg>SportsBook</li>
      <li><svg width="14" height="12" viewBox="0 0 14 12"><path d="M1 6 L5 10 L13 1" fill="none" stroke="#fff" stroke-width="2"/></svg>Full Support</li>
    </ul>
    <div class="agent" role="img" aria-label="Photograph of a support agent wearing a headset"></div>
  </section>

  <div class="abs join-badge"><span>JOIN NOW</span></div>
  <p class="abs join-text">Join the VR4LO CLUB Membership and Rewards Program today to start earning income with a new dedicated Gaming and Sport Betting Service directed to the networking industry.</p>
  <p class="abs packages-lead">we have these below packages...</p>
  <ul class="abs packages">
    <li>BRONZE</li><li>SILVER</li><li>GOLD</li><li>RUBY</li><li>EMRALD</li><li>DIAMOND</li>
  </ul>

  <div class="abs stat-band">
    <p class="lead">By 2016 the size of the online global games market is forecasted to reach</p>
    <p class="figure">$86.1 BILLION</p>
  </div>

  <p class="abs closing">You need to be a part of something to understand its advantages. All our customers have had that experience, which has made them stronger and adept at extracting maximum mileage from our platform in terms of excitement and revenue. Turn is simply yours now!</p>
  <a class="abs btn btn-join">Join now for anything please
    <svg width="22" height="22" viewBox="0 0 22 22"><circle cx="11" cy="11" r="10" fill="#fff"/><path d="M6 11 H15 M11 7 L15 11 L11 15" fill="none" stroke="#15b39b" stroke-width="2.2"/></svg>
  </a>

  <div class="abs divider"></div>

  <p class="abs social-lead">Get connected by us</p>
  <ul class="abs social-row" aria-label="Social network links">
    <li></li><li></li><li></li><li></li>
  </ul>
  <div class="abs footer-brand"><span>VR4LO ENT</span><span class="mark"></span></div>
  <p class="abs copyright">Copyright © Vr4lo Amusements - All Rights Reserved</p>
</body>
</html>
```